Lightweight, clean Wordpress theme for fitness app website

Trek-Otter.com needs a new website.

Trek-Otter itself is a mobile fitness app and this website will support it and help to promote it with screenshots and descriptions of the app.

Attached is the logo. The main colours are the blue and white on the logo.

I need a fully functioning Wordpress theme for this website.

It needs to be clean, lightweight, fast loading and easy to maintain and build.
The theme should include the home page, pages and posts so that we can have the flexibility to do what we want.

It should work just as well on mobile as for desktop.

The target audience is all fitness lovers, female and male, any age.

Must Have:
- Wordpress theme.
- Pages, posts and a home page.
- Simple, clean & lightweight.
- Desktop & mobile styling
- See attachment for colours and fonts

Should Not Have:
- Bloated & slow loading designs

Target Market(s)

Fitness enthusiasts of all abilities.
Male / Female. Young & Old.
Should NOT use imagery of big body builders.

Industry/Entity Type

Fitness

Coding

Coded - Design and coding required

Number of Pages Required

3 page

Requirements
Must have
• Wordpress theme
• Landing / home page.
• Template for a page and a post.
• Simple, clean & fast loading.

```html
<!DOCTYPE html>
<html lang="en">
<head>
<meta charset="utf-8">
<title>Trek-Otter – Mobile Fitness App</title>
<link href="https://fonts.googleapis.com/css2?family=Montserrat:wght@500;600;700&family=Open+Sans:wght@400;600;700&display=swap" rel="stylesheet">
<style>
:root{
  --blue:#1581c8;
  --blue-dark:#0f6fae;
  --blue-band:#1a88cf;
  --ink:#222a33;
  --text:#5b6470;
  --muted:#8a929c;
  --line:#e3e6ea;
  --white:#ffffff;
  --foot-bg:#eeeff1;
  --hero-a:#1c1f22;
  --hero-b:#4a4e52;
}
*{margin:0;padding:0;box-sizing:border-box}
html,body{width:1200px;height:3536px;overflow:hidden}
body{position:relative;background:var(--white);font-family:"Open Sans",Arial,sans-serif;color:var(--text)}
.abs{position:absolute}
.heading{font-family:"Montserrat",Arial,sans-serif;font-weight:700;text-transform:uppercase;letter-spacing:.5px}
.center{text-align:center}

/* header */
.brand{left:140px;top:14px;width:120px;text-align:center}
.brand-mark{width:44px;height:44px;border-radius:50%;background:var(--blue);margin:0 auto 8px}
.brand-name{font-family:"Open Sans",Arial,sans-serif;font-weight:700;font-size:15px;color:var(--blue)}
.call{left:755px;top:22px;font-family:"Montserrat",sans-serif}
.call small{display:block;font-size:10px;color:var(--muted);padding-left:22px;letter-spacing:.5px}
.call strong{display:flex;align-items:center;gap:6px;font-size:20px;color:var(--blue);font-weight:700}
.demo-btn{left:943px;top:19px;width:125px;height:38px;background:var(--blue);color:#fff;font-size:12px;display:flex;align-items:center;justify-content:center;gap:6px;font-family:"Montserrat",sans-serif;font-weight:700;border-radius:2px}
.nav{top:78px;left:592px;display:flex;align-items:center;font-family:"Montserrat",sans-serif;font-size:12px;font-weight:700;color:var(--ink)}
.nav span{display:block;padding:7px 14px;margin-right:28px}
.nav .active{background:var(--blue);color:#fff}

/* hero */
.hero{left:0;top:118px;width:1200px;height:584px;background:linear-gradient(100deg,var(--hero-a) 0%,var(--hero-b) 45%,#2a2d30 70%,var(--hero-a) 100%)}
.hero-title{left:78px;top:470px;font-size:42px;color:#fff}
.hero-btn{left:80px;top:544px;width:257px;height:48px;background:var(--blue);color:#fff;font-size:18px;font-weight:600;display:flex;align-items:center;justify-content:center;gap:12px;font-family:"Montserrat",sans-serif}
.dots{left:547px;top:648px;display:flex;gap:16px}
.dots i{display:block;width:10px;height:10px;border-radius:50%;background:rgba(255,255,255,.55)}
.dots i:first-child{background:#fff}

/* welcome */
.section-title{color:var(--blue);font-size:27px;width:1200px;left:0}
.welcome-text{left:285px;top:826px;width:630px;font-size:14px;line-height:25px}
.services{left:0;top:950px;width:1200px;height:177px}
.service{position:absolute;top:0;height:177px;text-align:center}
.service h4{font-family:"Montserrat",sans-serif;font-size:13px;font-weight:700;color:var(--ink);margin-top:20px}
.service svg{margin-top:24px}
.service.featured{background:var(--blue);color:#fff}
.service.featured h4{color:#fff;margin-top:14px}
.service.featured p{font-size:13px;line-height:19px;padding:0 30px}
.divider-v{left:842px;top:970px;width:1px;height:138px;background:var(--line)}

/* features */
.features{left:0;top:1273px;width:1200px;height:601px;background:var(--blue-band)}
.features-title{left:141px;top:1352px;font-size:26px;color:#fff}
.feature{width:230px;color:#fff}
.feature h5{font-family:"Montserrat",sans-serif;font-size:15px;font-weight:700;text-transform:uppercase;margin-bottom:8px}
.feature p{font-size:12px;line-height:17px;color:#e6f1fa}
.feature-icon{color:#fff}

/* phone */
.phone{left:460px;top:1207px;width:290px;height:596px;background:#fff;border-radius:38px;box-shadow:0 10px 30px rgba(0,0,0,.18);border:1px solid #e6e6e6}
.screen{position:absolute;left:7px;top:61px;width:276px;height:488px;background:#fff;overflow:hidden;border:1px solid #eee}
.app-bar{height:30px;background:var(--blue);color:#fff;font-size:11px;font-weight:700;display:flex;align-items:center;padding:0 12px;gap:10px}
.status{height:16px;background:var(--blue-dark)}
.app-search{margin:6px 8px;height:20px;border:1px solid #ccd;font-size:9px;color:#99a;padding:3px 6px}
.month{text-align:center;font-size:11px;color:var(--blue);font-weight:700;margin:8px 0 4px}
.cal{display:grid;grid-template-columns:repeat(7,1fr);font-size:9px;text-align:center;row-gap:10px;padding:0 8px;color:#444}
.cal .d{color:#999}
.cal .on{background:var(--blue);color:#fff;border-radius:50%;width:16px;height:16px;line-height:16px;margin:-3px auto 0}
.recent{margin-top:14px;background:#f0f1f3;font-size:9px;color:#889;padding:4px 8px}
.row{display:flex;justify-content:space-between;font-size:9px;color:#556;padding:7px 10px;border-bottom:1px solid #eee}
.row b{color:var(--blue);font-weight:600}
.fab{position:absolute;right:14px;bottom:22px;width:30px;height:30px;border-radius:50%;background:var(--blue);color:#fff;text-align:center;line-height:30px;font-size:18px}
.home-key{left:113px;top:560px;width:64px;height:24px;border-radius:12px;background:var(--blue)}

/* mobile app */
.app-photo{left:0;top:1878px;width:966px;height:585px;background:linear-gradient(90deg,#5a6b70 0%,#7d8b8a 35%,#b9c0bd 62%,#ffffff 100%)}
.callout{background:#fff;padding:10px 14px;box-shadow:0 2px 8px rgba(0,0,0,.18);font-size:12px;line-height:17px;color:var(--text)}
.callout b{display:block;font-family:"Montserrat",sans-serif;font-size:12px;color:var(--blue);margin-bottom:3px}
.app-title{left:700px;top:1950px;font-size:26px;color:var(--blue)}
.app-text{left:700px;top:1998px;width:400px;font-size:13px;line-height:24px}
.app-list{left:700px;top:2100px;list-style:none;font-size:15px;color:var(--ink)}
.app-list li{height:30px;display:flex;align-items:center;gap:14px}
.app-list li::before{content:"";border-left:7px solid var(--blue);border-top:5px solid transparent;border-bottom:5px solid transparent}
.available{left:818px;top:2254px;width:134px;height:30px;border:1px solid #cfd3d8;font-size:11px;font-weight:700;color:var(--ink);display:flex;align-items:center;justify-content:center;font-family:"Montserrat",sans-serif}
.store-badge{top:2322px;height:56px;background:#111;border-radius:7px}

/* blog */
.blog-card{top:2607px;width:295px;height:403px;border:1px solid var(--line);background:#fff;text-align:center}
.blog-img{height:205px}
.blog-card h3{font-family:"Montserrat",sans-serif;font-size:13px;font-weight:700;color:var(--ink);text-transform:uppercase;line-height:19px;margin:30px 40px 12px}
.blog-card p{font-size:12px;line-height:17px;padding:0 40px}
.read-btn{display:inline-block;margin-top:18px;background:var(--blue);color:#fff;font-size:11px;font-weight:700;font-family:"Montserrat",sans-serif;padding:6px 14px}

/* newsletter & footer */
.footer-bg{left:0;top:3142px;width:1200px;height:394px;background:var(--foot-bg)}
.newsletter{left:222px;top:3076px;width:754px;height:148px;background:var(--blue)}
.newsletter h2{position:absolute;left:47px;top:34px;color:#fff;font-size:21px}
.field{position:absolute;top:75px;height:40px;background:#fff;font-size:12px;color:#777;padding:11px 14px}
.signup{position:absolute;left:556px;top:75px;width:160px;height:40px;border:2px solid #fff;color:#fff;font-family:"Montserrat",sans-serif;font-weight:700;font-size:15px;display:flex;align-items:center;justify-content:center}
.foot-brand{left:216px;top:3296px;width:120px;text-align:center}
.foot-h{font-family:"Montserrat",sans-serif;font-size:12px;font-weight:700;color:var(--blue);text-transform:uppercase}
.foot-list{font-size:12px;line-height:23px;color:#555;list-style:none}
.menu-list{line-height:15px}
.social{display:flex;gap:10px}
.social i{display:block;width:28px;height:28px;border-radius:50%}
.copy-line{left:0;top:3465px;width:1200px;height:1px;background:#dcdfe3}
.copy{left:0;top:3488px;width:1200px;font-size:11px;color:#555}
</style>
</head>
<body>

<!-- header -->
<div class="abs brand">
  <div class="brand-mark"></div>
  <div class="brand-name">Trek-Otter.com</div>
</div>
<div class="abs call">
  <small>CALL US</small>
  <strong><svg width="16" height="16" viewBox="0 0 24 24" fill="currentColor"><path d="M6.6 10.8a15 15 0 0 0 6.6 6.6l2.2-2.2c.3-.3.7-.4 1-.2 1.1.4 2.3.6 3.6.6.6 0 1 .4 1 1V20c0 .6-.4 1-1 1A17 17 0 0 1 3 4c0-.6.4-1 1-1h3.5c.6 0 1 .4 1 1 0 1.3.2 2.5.6 3.6.1.3 0 .7-.2 1z"/></svg>1.800.555.0142</strong>
</div>
<div class="abs demo-btn"><svg width="12" height="12" viewBox="0 0 24 24" fill="none" stroke="#fff" stroke-width="2.5"><rect x="3" y="4" width="18" height="13"/><path d="M8 21h8"/></svg>SEE A DEMO</div>
<nav class="abs nav">
  <span class="active">HOME</span><span>ABOUT US</span><span>BLOG</span><span>THE APP</span><span>CONTACT US</span>
</nav>

<!-- hero -->
<div class="abs hero" role="img" aria-label="Photo of a person training on a cable machine in a dim gym"></div>
<div class="abs heading hero-title">Trek-Otter</div>
<div class="abs hero-btn">READ MORE <svg width="10" height="12" viewBox="0 0 10 12"><path d="M0 0l10 6-10 6z" fill="#fff"/></svg></div>
<div class="abs dots"><i></i><i></i><i></i><i></i><i></i></div>

<!-- welcome -->
<h1 class="abs heading section-title center" style="top:762px">Welcome to our site</h1>
<p class="abs welcome-text center">There are many variations of passages of Lorem Ipsum available, but the majority have suffered alteration in some form, by injected humour, or randomised words which don't look even slightly believable. If you are going to use a passage of Lorem Ipsum, you need to be sure there</p>

<div class="abs services">
  <div class="service" style="left:143px;width:200px">
    <svg width="40" height="62" viewBox="0 0 40 62" fill="none" stroke="var(--blue)" stroke-width="3"><rect x="4" y="2" width="32" height="58" rx="4"/><circle cx="20" cy="26" r="5" fill="var(--blue)"/><path d="M11 42c2-7 16-7 18 0"/><path d="M15 53h10"/></svg>
    <h4>BOOK TRAINING</h4>
  </div>
  <div class="service featured" style="left:360px;width:250px">
    <svg width="72" height="58" viewBox="0 0 72 58" fill="#fff"><circle cx="36" cy="10" r="8"/><path d="M18 20h36l8-10 8 4-10 18H48v24H24V32H12L2 14l8-4z"/></svg>
    <h4>FOLLOW TRAINERS</h4>
    <p>There are many variations of passages of Lorem</p>
  </div>
  <div class="service" style="left:624px;width:200px">
    <svg width="64" height="62" viewBox="0 0 64 62" fill="var(--blue)"><rect x="4" y="22" width="8" height="18" rx="2"/><rect x="12" y="16" width="8" height="30" rx="2"/><rect x="20" y="28" width="24" height="6"/><rect x="44" y="16" width="8" height="30" rx="2"/><rect x="52" y="22" width="8" height="18" rx="2"/></svg>
    <h4>WORKOUTS</h4>
  </div>
  <div class="service" style="left:843px;width:200px">
    <svg width="62" height="62" viewBox="0 0 62 62" fill="none" stroke="var(--blue)" stroke-width="3.5"><circle cx="29" cy="33" r="24"/><circle cx="29" cy="33" r="15"/><circle cx="29" cy="33" r="6" fill="var(--blue)"/><path d="M29 33L54 8M48 6l6 2 2 6"/></svg>
    <h4>FITNESS GOAL</h4>
  </div>
</div>
<div class="abs divider-v"></div>

<!-- features -->
<section class="abs features"></section>
<h2 class="abs heading features-title">Features</h2>

<svg class="abs feature-icon" style="left:140px;top:1424px" width="38" height="38" viewBox="0 0 38 38" fill="none" stroke="#fff" stroke-width="3"><circle cx="15" cy="15" r="11"/><path d="M23 23l12 12"/></svg>
<div class="abs feature" style="left:226px;top:1424px"><h5>Find an Instructor</h5><p>There are many variations of passages of Lorem Ipsum available, but the by inje.</p></div>

<svg class="abs feature-icon" style="left:138px;top:1554px" width="42" height="36" viewBox="0 0 42 36" fill="none" stroke="#fff" stroke-width="3"><rect x="2" y="2" width="38" height="32"/><path d="M2 10h38M9 17h6M9 24h6M19 17h14M19 24h14"/></svg>
<div class="abs feature" style="left:226px;top:1554px"><h5>Manage Bookings</h5><p>There are many variations of passages of Lorem Ipsum available, but the by inje.</p></div>

<svg class="abs feature-icon" style="left:136px;top:1694px" width="46" height="38" viewBox="0 0 46 38" fill="#fff"><circle cx="23" cy="6" r="5"/><rect x="18" y="13" width="10" height="14" rx="2"/><circle cx="9" cy="12" r="4"/><rect x="5" y="18" width="8" height="12" rx="2"/><circle cx="37" cy="12" r="4"/><rect x="33" y="18" width="8" height="12" rx="2"/><rect x="0" y="32" width="46" height="3"/></svg>
<div class="abs feature" style="left:226px;top:1694px"><h5>Group Coaching</h5><p>There are many variations of passages of Lorem Ipsum available, but the by inje.</p></div>

<svg class="abs feature-icon" style="left:806px;top:1424px" width="40" height="40" viewBox="0 0 40 40" fill="none" stroke="#fff" stroke-width="3"><circle cx="14" cy="14" r="10"/><path d="M14 14l6 22 4-8 8 8 4-4-8-8 8-4z" fill="#fff"/></svg>
<div class="abs feature" style="left:879px;top:1424px"><h5>Ways to Book</h5><p>There are many variations of passages of Lorem Ipsum available, but the by inje.</p></div>

<svg class="abs feature-icon" style="left:808px;top:1552px" width="36" height="40" viewBox="0 0 36 40" fill="none" stroke="#fff" stroke-width="3"><path d="M6 30V17a12 12 0 0 1 24 0v13l4 4H2z"/><path d="M14 37h8"/></svg>
<div class="abs feature" style="left:879px;top:1554px"><h5>Class Schedules</h5><p>There are many variations of passages of Lorem Ipsum available, but the by inje.</p></div>

<svg class="abs feature-icon" style="left:810px;top:1692px" width="32" height="44" viewBox="0 0 32 44" fill="#fff"><path d="M16 0a15 15 0 0 0-15 15c0 11 15 29 15 29s15-18 15-29A15 15 0 0 0 16 0zm0 21a6 6 0 1 1 0-12 6 6 0 0 1 0 12z"/></svg>
<div class="abs feature" style="left:879px;top:1694px"><h5>Workout Tracking</h5><p>There are many variations of passages of Lorem Ipsum available, but the by inje.</p></div>

<div class="abs phone">
  <div class="screen">
    <div class="status"></div>
    <div class="app-bar">☰ <span>Trek-Otter</span></div>
    <div class="app-search">Select a day to view sessions</div>
    <div class="month">2017 May</div>
    <div class="cal">
      <span>Sun</span><span>Mon</span><span>Tue</span><span>Wed</span><span>Thu</span><span>Fri</span><span>Sat</span>
      <span class="d">30</span><span>1</span><span>2</span><span>3</span><span>4</span><span>5</span><span>6</span>
      <span>7</span><span>8</span><span><span class="on" style="display:block">9</span></span><span>10</span><span><span class="on" style="display:block">11</span></span><span>12</span><span>13</span>
      <span>14</span><span>15</span><span>16</span><span>17</span><span>18</span><span>19</span><span>20</span>
      <span>21</span><span>22</span><span>23</span><span>24</span><span>25</span><span>26</span><span>27</span>
      <span>28</span><span>29</span><span>30</span><span>31</span><span class="d">1</span><span class="d">2</span><span class="d">3</span>
    </div>
    <div class="recent">Recent sessions</div>
    <div class="row"><b>09 May 2017</b><span>Task 1</span></div>
    <div class="row"><b>09 May 2017</b><span>Task 2</span></div>
    <div class="row"><b>10 May 2017</b><span>Task 3</span></div>
    <div class="row"><b>11 May 2017</b><span>Task 4</span></div>
    <div class="row"><b>11 May 2017</b><span>Task 5</span></div>
    <div class="fab">+</div>
  </div>
  <div class="abs home-key"></div>
</div>

<!-- mobile app -->
<div class="abs app-photo" role="img" aria-label="Photo of a hand holding a phone showing the app calendar"></div>
<div class="abs callout" style="left:57px;top:1928px;width:226px"><b>MENU</b>There are many variations of passages of Lorem</div>
<div class="abs callout" style="left:318px;top:2074px;width:198px"><b>BOOKED STATUS</b>There are many variations of passages of Lorem</div>
<div class="abs callout" style="left:28px;top:2286px;width:231px"><b>SESSIONS</b>There are many variations of passages of Lorem</div>

<h2 class="abs heading app-title">Mobile Fitness App</h2>
<p class="abs app-text">There are many variations of passages of Lorem Ipsum available, but the majority have suffered alteration in some form, by injected humour, or randomised w</p>
<ul class="abs app-list">
  <li>It is a long established</li>
  <li>There are many variations</li>
  <li>Contrary to popular belief</li>
  <li>Lorem Ipsum is simply dumm</li>
</ul>
<div class="abs available">NOW AVAILABLE AT</div>
<div class="abs store-badge" style="left:707px;width:179px"></div>
<div class="abs store-badge" style="left:898px;width:174px"></div>

<!-- blog -->
<h2 class="abs heading section-title center" style="top:2525px">Latest Blog</h2>
<article class="abs blog-card" style="left:134px">
  <div class="blog-img" role="img" aria-label="Photo of people doing push-ups in a gym class" style="background:linear-gradient(135deg,#3a3633,#7a6e66)"></div>
  <h3>Contrary to popular belief Lorem Ipsum</h3>
  <p>page editors now use Lorem Ipsum as their default model text, and a search</p>
  <span class="read-btn">READ MORE</span>
</article>
<article class="abs blog-card" style="left:455px">
  <div class="blog-img" role="img" aria-label="Photo of an athlete lifting a barbell with chalk dust" style="background:linear-gradient(135deg,#1a2230,#4c5a6e)"></div>
  <h3>Lorem Ipsum is simply dummy</h3>
  <p>If you are going to use a passage of Lorem Ipsum, you need to be sure there isn't</p>
  <span class="read-btn">READ MORE</span>
</article>
<article class="abs blog-card" style="left:775px">
  <div class="blog-img" role="img" aria-label="Photo of a woman training with a kettlebell" style="background:linear-gradient(135deg,#2a1a12,#8a5a36)"></div>
  <h3>It is a long established fact</h3>
  <p>page editors now use Lorem Ipsum as their default model text, and a search</p>
  <span class="read-btn">READ MORE</span>
</article>

<!-- newsletter & footer -->
<div class="abs footer-bg"></div>
<section class="abs newsletter">
  <h2 class="heading">Newsletter Signup</h2>
  <div class="field" style="left:44px;width:238px">Name</div>
  <div class="field" style="left:294px;width:238px">E-mail id</div>
  <div class="signup">SIGNUP</div>
</section>

<div class="abs foot-brand">
  <div class="brand-mark"></div>
  <div class="brand-name" style="font-size:14px">Trek-Otter.com</div>
</div>
<div class="abs" style="left:412px;top:3286px">
  <div class="foot-h">Contact Us</div>
  <ul class="foot-list" style="margin-top:20px">
    <li>48 Alder Lane, Brookfield, OR 97411</li>
    <li>T : 1.800.555.0142</li>
    <li>E : info@trek-otter.com</li>
  </ul>
</div>
<div class="abs" style="left:726px;top:3286px">
  <div class="foot-h">Menu</div>
  <ul class="foot-list menu-list" style="margin-top:16px;font-size:12px">
    <li>Home</li><li>About us</li><li>Blog</li><li>The App</li><li>Contact us</li>
  </ul>
</div>
<div class="abs" style="left:874px;top:3286px">
  <div class="foot-h">Follow Us</div>
  <div class="social" style="margin-top:24px">
    <i style="background:#3b5998"></i><i style="background:#1da1f2"></i><i style="background:#dd4b39"></i>
  </div>
</div>
<div class="abs copy-line"></div>
<div class="abs copy center">Copyright @ 2017 All Rights Reserved</div>

</body>
</html>
```